Corporate Branding - Web and Print

A UK based company will like to use an existing logo to create branding materials for all marketing related documents, including business card, prints, letterhead, Website, Twitter, Facebook, Instagram logo etc. This company serves high-end clientele in the fashion, health and wellness and as such high quality and class is of utmost importance.
Where the logo can be modernised without losing its character then experiment. The main thing is to have a corporate branding which can be used later for brochures, Business Plan infographics.
The prominent colour within the organisation is burnt orange with no secondary colour. However if you believe a secondary colour is needed then use it, otherwise keep it simple and classy. Any chosen colours have to match perfectly.
Target Market(s)
High net worth individuals
Industry/Entity Type
Health And Wellness
Contact Information for Business Card
classy

```html
<!DOCTYPE html>
<html lang="en">
<head>
<meta charset="utf-8">
<title>Velmora Business Card</title>
<link href="https://fonts.googleapis.com/css2?family=Roboto:wght@300;400;700&display=swap" rel="stylesheet">
<style>
  :root {
    --backdrop: #5d6266;
    --orange: #f7941e;
    --orange-deep: #f26a21;
    --white: #ffffff;
    --ink: #1d1d1d;
  }
  * { margin: 0; padding: 0; box-sizing: border-box; }
  html, body { width: 1200px; height: 900px; overflow: hidden; }
  body {
    background: var(--backdrop);
    font-family: "Roboto", sans-serif;
    display: flex;
    align-items: center;
    justify-content: center;
    gap: 40px;
  }
  .card {
    position: relative;
    width: 540px;
    height: 310px;
    border-radius: 14px;
    overflow: hidden;
  }
  .card-shapes { position: absolute; inset: 0; }

  /* Front */
  .card-front { background: var(--white); }
  .brand {
    position: absolute;
    display: flex;
    align-items: center;
    gap: 10px;
    color: var(--orange-deep);
    font-weight: 700;
    white-space: nowrap;
  }
  .card-front .brand { left: 150px; top: 34px; font-size: 40px; letter-spacing: 1px; }
  .brand-dot { border-radius: 50%; background: currentColor; flex: none; }
  .card-front .brand-dot { width: 34px; height: 34px; }

  .contact-list {
    position: absolute;
    left: 30px;
    top: 104px;
    list-style: none;
    font-size: 14px;
    color: var(--ink);
  }
  .contact-list li { display: flex; align-items: center; gap: 10px; height: 22px; white-space: nowrap; }
  .contact-icon {
    width: 16px; height: 16px;
    background: var(--orange);
    border-radius: 2px;
    display: flex; align-items: center; justify-content: center;
    flex: none;
  }
  .address {
    position: absolute;
    left: 30px;
    bottom: 40px;
    font-size: 14px;
    color: var(--white);
    white-space: nowrap;
  }
  .person {
    position: absolute;
    right: 48px;
    top: 120px;
    text-align: left;
  }
  .person-name { font-size: 20px; font-weight: 300; color: var(--orange); letter-spacing: 0.5px; white-space: nowrap; }
  .person-role { font-size: 12px; color: var(--ink); }

  /* Back */
  .card-back { background: var(--orange); }
  .card-back .brand {
    color: var(--white);
    left: 50%; top: 50%;
    transform: translate(-50%, -50%);
    font-size: 64px;
    gap: 16px;
    letter-spacing: 2px;
  }
  .card-back .brand-dot { width: 56px; height: 56px; }
</style>
</head>
<body>

<section class="card card-back" aria-label="Business card back">
  <div class="brand"><span class="brand-dot"></span><span class="brand-name">VELMORA</span></div>
</section>

<section class="card card-front" aria-label="Business card front">
  <svg class="card-shapes" width="540" height="310" viewBox="0 0 540 310">
    <polygon points="0,190 250,222 540,178 540,310 0,310" fill="var(--orange)"/>
    <line x1="170" y1="232" x2="540" y2="176" stroke="var(--orange-deep)" stroke-width="4"/>
    <polygon points="505,0 540,0 540,95" fill="var(--orange)"/>
    <line x1="498" y1="0" x2="540" y2="104" stroke="var(--orange-deep)" stroke-width="3"/>
  </svg>

  <div class="brand"><span class="brand-dot"></span><span class="brand-name">VELMORA</span></div>

  <ul class="contact-list">
    <li>
      <span class="contact-icon">
        <svg width="10" height="10" viewBox="0 0 10 10"><path d="M2 1 L4 1 L4.5 3 L3.3 3.8 Q4.3 5.8 6.2 6.7 L7 5.5 L9 6 L9 8 Q5 9 2.5 6 Q1 4 2 1Z" fill="#fff"/></svg>
      </span>020-555-0148
    </li>
    <li>
      <span class="contact-icon">
        <svg width="10" height="10" viewBox="0 0 10 10"><rect x="1" y="2.5" width="8" height="5.5" fill="none" stroke="#fff" stroke-width="1"/><path d="M1 2.5 L5 5.5 L9 2.5" fill="none" stroke="#fff" stroke-width="1"/></svg>
      </span>hello@velmora.co
    </li>
    <li>
      <span class="contact-icon">
        <svg width="10" height="10" viewBox="0 0 10 10"><circle cx="5" cy="5" r="3.8" fill="none" stroke="#fff" stroke-width="1"/><path d="M1.2 5 H8.8 M5 1.2 Q3 5 5 8.8 M5 1.2 Q7 5 5 8.8" fill="none" stroke="#fff" stroke-width="0.8"/></svg>
      </span>www.velmora.co
    </li>
  </ul>

  <p class="address">18 Harrow Lane, London W1 4QT</p>

  <div class="person">
    <p class="person-name">CLARA BENNETT</p>
    <p class="person-role">OWNER</p>
  </div>
</section>

</body>
</html>
```